Professional Oral Surgery Referral Pad, Business Card, and Stationary Design

Hello,

I want to work with a designer for my startup Oral Surgery Practice called: Dorrel Creek Oral Surgery & Implant Center

Ideally I would like to choose a good/professional design and work with a designer all the way to fulfill ALL of our stationary needs including referral pads, business cards, letterheads, envelopes, notepads, email signature, etc.

I would like to see designs first and hopefully would like to work with the designer for the lifetime of my practice and wanting to develop a long-term professional relationship.

In terms of the logo I have attached our practice logo files: I want to stay within the 3 colorways of the logo: Navy Blue/Silver grey/White. I would like for you to be creative and incorporate the "V" as best you can (for example greyed out watermark, etc)

I have also attached in my files the full contact info of our office in a word document: which includes address, email address, phone, fax, cell, etc.

I have also attached a few examples of double sided referral pad we can draw inspiration from. In terms of the referral pad I would ideally like to have my logo nicely placed/incorporated to make it look professional, address of the practice and contact info, my name and credentials.

Referral pad must have lines for patient, date of birth, phone number, referring doctor name, odontogram of all adult teeth and pediatric teeth, nice and big - so easy for dentist to refer. Also a jaw drawing of the intraoral cavity. Below that should have comments to surgeon.

In terms of procedures, I would like to have options of IV sedation, extractions, wisdom teeth, bone graft, pathology, tmj, trauma, expose/bond, orthognathic, other (list below)

In the back we can have a greyed out map of my practice address and Instructions for patients should include to bring insurance documentation, medication list, etc.

The final nitty gritty details of the referral pad can be worked on once I am happy with the design.

Target Market(s)

Patients who need oral surgical services and dentist referrals

Industry/Entity Type

Oral and Maxillofacial Surgery

• I would leave it up to the designers!

Colors
0054AA
0677BA
7BADD7
CADEEF
E8F1F8

Requirements
Must have
• Professional/sleek/modern and three color ways same as logo (navy blue, silver gray, and white)
Nice to have
• I would like to highlight my logo especially the implant ā€œvā€ either as watermark or part of the header or footnote. I will leave it to the expertise of the designer

```html
<!DOCTYPE html>
<html lang="en">
<head>
<meta charset="utf-8">
<title>Dorrel Creek Oral Surgery – Business Card</title>
<link href="https://fonts.googleapis.com/css2?family=EB+Garamond:ital,wght@0,400;0,500;0,600;1,400&display=swap" rel="stylesheet">
<style>
  :root {
    --navy: #003a8a;
    --white: #ffffff;
    --stage: #8f8f8f;
    --ink: #1f3f94;
  }
  * { box-sizing: border-box; margin: 0; padding: 0; }
  html, body { width: 1200px; height: 1200px; overflow: hidden; }
  body {
    background: var(--stage);
    font-family: "EB Garamond", Georgia, serif;
    position: relative;
  }
  .card {
    position: absolute;
    left: 250px;
    width: 700px;
    height: 400px;
    border-radius: 22px;
    background: var(--white);
    overflow: hidden;
    box-shadow: 0 2px 6px rgba(0,0,0,.25);
  }
  .card--front { top: 170px; }
  .card--back { top: 631px; color: var(--ink); }

  .front-panel { position: absolute; inset: 0; }

  .doctor { position: absolute; left: 47px; top: 84px; color: var(--white); }
  .doctor__name { font-size: 27px; font-weight: 600; letter-spacing: .3px; line-height: 1; }
  .doctor__practice { font-size: 18px; font-style: italic; margin-top: 8px; letter-spacing: .2px; }

  .contact { position: absolute; left: 44px; top: 168px; color: var(--white); list-style: none; }
  .contact li { display: flex; align-items: flex-start; font-size: 18px; letter-spacing: .6px; line-height: 24px; margin-bottom: 2px; }
  .contact li.contact__phone { font-size: 20px; letter-spacing: 1.6px; }
  .contact svg { width: 16px; height: 16px; flex: none; margin: 4px 11px 0 0; fill: var(--white); }

  .front-name {
    position: absolute; left: 560px; top: 186px; transform: translateX(-50%);
    font-size: 38px; font-weight: 600; color: var(--navy); white-space: nowrap;
  }

  .back-name {
    position: absolute; left: 0; right: 0; top: 58px; text-align: center;
    font-size: 25px; font-weight: 600; color: var(--navy); letter-spacing: .4px;
  }

  .field-row { position: absolute; left: 41px; right: 41px; display: flex; align-items: baseline; font-size: 20px; }
  .field-row .leader { flex: 1; border-bottom: 1.5px dotted var(--ink); margin: 0 1px; transform: translateY(-4px); }
  .field-row .suffix { font-size: 17px; }
  .row-datetime { top: 134px; }
  .row-comments { top: 242px; left: 44px; right: 42px; }
  .row-blank { top: 296px; left: 44px; right: 42px; height: 2px; border-bottom: 1.5px dotted var(--ink); }

  .days { position: absolute; top: 186px; left: 0; right: 0; display: flex; justify-content: center; gap: 21px; font-size: 20px; }
  .day { display: flex; align-items: center; }
  .day__box { width: 15px; height: 15px; border: 2px solid var(--ink); margin-right: 4px; }

  .notice { position: absolute; left: 0; right: 0; top: 332px; text-align: center; font-size: 14.5px; font-style: italic; line-height: 16px; }
</style>
</head>
<body>

<section class="card card--front">
  <svg class="front-panel" viewBox="0 0 700 400" aria-hidden="true">
    <path d="M0 0 H262 C298 2 318 22 335 58 L475 400 H0 Z" fill="var(--navy)"/>
  </svg>

  <div class="doctor">
    <h1 class="doctor__name">Dr. Anil Varma, DDS</h1>
    <p class="doctor__practice">Dorrel Creek Oral Surgery &amp; Implant Center</p>
  </div>

  <ul class="contact">
    <li>
      <svg viewBox="0 0 16 16"><path d="M8 0a5.5 5.5 0 0 0-5.5 5.5C2.5 9.7 8 16 8 16s5.5-6.3 5.5-10.5A5.5 5.5 0 0 0 8 0zm0 8a2.5 2.5 0 1 1 0-5 2.5 2.5 0 0 1 0 5z"/></svg>
      <span>218 Birchwood Ave<br>Dorrel Creek, CA 91502</span>
    </li>
    <li class="contact__phone">
      <svg viewBox="0 0 16 16"><path d="M3.5 1l2.5 3-1.5 2a9 9 0 0 0 5 5l2-1.5 3 2.5-1.5 2.5C7 15 1 9 1 2.5z"/></svg>
      <span>818 555 0142</span>
    </li>
    <li class="contact__phone">
      <svg viewBox="0 0 16 16"><path d="M4 1h8v4H4zM1 6h14v7h-3v2H4v-2H1zm4 4v4h6v-4z"/></svg>
      <span>818 555 0147</span>
    </li>
    <li>
      <svg viewBox="0 0 16 16"><path d="M1 4h14v9H1zm1 1 6 4.5L14 5z"/></svg>
      <span>info@dorrelcreekoms.com</span>
    </li>
    <li>
      <svg viewBox="0 0 16 16"><circle cx="8" cy="8" r="7.5"/><path d="M4 4c2 1 1 3 3 3s1 3 2 4M10 2c0 2 2 2 3 3" stroke="var(--navy)" stroke-width="1.3" fill="none"/></svg>
      <span>dorrelcreekoms.com</span>
    </li>
  </ul>

  <div class="front-name">Dorrel Creek</div>
</section>

<section class="card card--back">
  <div class="back-name">Dorrel Creek Oral Surgery &amp; Implant Center</div>

  <div class="field-row row-datetime">
    <span>DATE</span><span class="leader"></span><span>TIME</span><span class="leader"></span><span class="suffix">AM\PM</span>
  </div>

  <div class="days">
    <span class="day"><span class="day__box"></span>MON</span>
    <span class="day"><span class="day__box"></span>TUES</span>
    <span class="day"><span class="day__box"></span>WED</span>
    <span class="day"><span class="day__box"></span>THU</span>
    <span class="day"><span class="day__box"></span>FRI</span>
    <span class="day"><span class="day__box"></span>SAT</span>
  </div>

  <div class="field-row row-comments">
    <span>COMMENTS</span><span class="leader"></span>
  </div>
  <div class="field-row row-blank"></div>

  <p class="notice">If you are unable to keep your appointment, please call us to<br>reschedule at least 48 hours prior to your appointment.</p>
</section>

</body>
</html>
```